kleines Trainingsinstitut sucht Visitenkartendesign
Zielgruppe
Wir sind ein kleines Trainigsinstitut und bieten Englisch- und interkulturelle Trainings. Zielgruppe sind v.a. Firmen.
Aufgabenstellung
Es sollte klar werden, dass CVW die Abkürzung von Clear Voice Workshop ist. (Schrift blippo)
Das Siegel (Qualitiät, Transpaenz, Integrität) sollte deutlich sichtbar, aber nicht allzu aufdringlich sein.
Im Anhang schicke ich Ihnen einen Entwurf, der mir noch verbesserungsfähig scheint.
Obwohl ich eigentlich Blautöne bevorzuge, können Sie auch mit der Farbe spielen (evtl. in Kombination mit orange). Bitte max. drei Farben.

```html
<!DOCTYPE html>
<html lang="de">
<head>
<meta charset="utf-8">
<title>CVW Visitenkarte</title>
<link href="https://fonts.googleapis.com/css2?family=Arimo:wght@400;700&display=swap" rel="stylesheet">
<style>
  :root {
    --brand-blue: #0a3a78;
    --accent-orange: #f0ac3a;
    --paper: #ffffff;
    --page-bg: #ffffff;
    --seal-blue: #2f6fc0;
  }
  html, body {
    margin: 0;
    padding: 0;
    width: 800px;
    height: 1200px;
    overflow: hidden;
    background: var(--page-bg);
    font-family: "Arimo", Arial, sans-serif;
  }
  .canvas {
    position: relative;
    width: 800px;
    height: 1200px;
  }
  .card {
    position: absolute;
    width: 497px;
    height: 320px;
    box-shadow: 6px 8px 18px rgba(0, 0, 0, 0.22);
    overflow: hidden;
  }
  /* front */
  .card-front {
    left: 60px;
    top: 300px;
    background: var(--paper);
    z-index: 2;
  }
  .front-band {
    position: absolute;
    left: 0; top: 0;
    width: 100%;
    height: 123px;
    background: var(--brand-blue);
  }
  .front-rule {
    position: absolute;
    left: 0; top: 117px;
    width: 310px;
    height: 6px;
    background: var(--accent-orange);
  }
  .front-logo {
    position: absolute;
    left: 46px;
    top: 18px;
    font-weight: 700;
    font-size: 64px;
    line-height: 1;
    color: var(--paper);
    letter-spacing: 1px;
  }
  .front-tagline {
    position: absolute;
    left: 203px;
    top: 48px;
    font-weight: 700;
    font-size: 14px;
    line-height: 15px;
    color: var(--paper);
    letter-spacing: 0.3px;
  }
  .front-tagline .level {
    display: block;
    color: var(--accent-orange);
    font-size: 12px;
    letter-spacing: 0.8px;
  }
  .quality-seal {
    position: absolute;
    left: 431px;
    top: 54px;
  }
  .contact-person {
    position: absolute;
    left: 49px;
    top: 185px;
    color: var(--brand-blue);
  }
  .contact-name {
    font-weight: 700;
    font-size: 17px;
    margin: 0 0 7px;
  }
  .contact-role {
    font-size: 12.5px;
    line-height: 17px;
    margin: 0;
  }
  .contact-address {
    position: absolute;
    left: 49px;
    top: 264px;
    font-size: 10.5px;
    font-weight: 700;
    color: var(--brand-blue);
  }
  .contact-phone {
    position: absolute;
    left: 311px;
    top: 171px;
    font-size: 11.5px;
    line-height: 17px;
    color: var(--brand-blue);
  }
  .contact-phone b { font-weight: 700; margin-right: 4px; }
  .contact-online {
    position: absolute;
    right: 55px;
    top: 246px;
    text-align: right;
    font-size: 10.5px;
    font-weight: 700;
    line-height: 19px;
    color: var(--brand-blue);
  }
  /* back */
  .card-back {
    left: 250px;
    top: 578px;
    background: var(--brand-blue);
    z-index: 1;
  }
  .back-logo {
    position: absolute;
    left: 0; right: 0;
    top: 100px;
    text-align: center;
    font-weight: 700;
    font-size: 84px;
    line-height: 1;
    color: var(--paper);
    letter-spacing: 2px;
  }
  .back-url {
    position: absolute;
    left: 0; right: 0;
    top: 194px;
    text-align: center;
    font-weight: 700;
    font-size: 15.5px;
    color: var(--accent-orange);
  }
  .back-services {
    position: absolute;
    left: 0; right: 0;
    top: 272px;
    text-align: center;
    font-size: 12.5px;
    font-weight: 700;
    color: var(--paper);
  }
</style>
</head>
<body>
<main class="canvas">
  <section class="card card-front" aria-label="Visitenkarte Vorderseite">
    <div class="front-band"></div>
    <div class="front-rule"></div>
    <div class="front-logo">CVW</div>
    <div class="front-tagline">Clear Voice Workshop<span class="level">PROFESSIONAL</span></div>
    <svg class="quality-seal" width="46" height="46" viewBox="0 0 46 46" role="img" aria-label="Qualitätssiegel">
      <circle cx="23" cy="23" r="22" fill="var(--seal-blue)"/>
      <circle cx="23" cy="23" r="15" fill="none" stroke="#ffffff" stroke-width="1.2" opacity="0.8"/>
    </svg>

    <div class="contact-person">
      <p class="contact-name">Helena Brandt</p>
      <p class="contact-role">Interkulturelles Training &amp; Coaching</p>
      <p class="contact-role">Clear Voice Workshop</p>
    </div>
    <div class="contact-address">Lindenweg 14 | 72180 Haag</div>
    <div class="contact-phone">
      <div><b>TEL</b>(07461) 55210–40</div>
      <div><b>FAX</b>(07461) 55210–41</div>
    </div>
    <div class="contact-online">
      <div>www.cvw-workshop.de</div>
      <div>Helena.Brandt@cvw-workshop.de</div>
    </div>
  </section>

  <section class="card card-back" aria-label="Visitenkarte Rückseite">
    <div class="back-logo">CVW</div>
    <div class="back-url">www.cvw-workshop.de</div>
    <div class="back-services">Interkulturelles Training &amp; Coaching — Clear Voice Workshop</div>
  </section>
</main>
</body>
</html>
```